Nonprofit K-8 Tillerby School. Elementary education ( please google Tillerby Schools)

We are a nonprofit Tillerby School in the U.S.
We need to advertise our school using yard signs. The information should be easy to see from a distance. Clear and concise, using large print without additional design outside of the logo itself. It should have our logo as the header, with the following text centered below the logo:
Open House!
Feb 10th, March 10th and April 21st.
Call 555 417-9086 for more information

Target Market(s)

Parents of children between ages of 5 yrs to 13yrs old

Industry/Entity Type

School

Font styles to use
Other font styles liked:
• Formal436bt

Colors
ec1f27
ffffff

Requirements
Must have
• It must have our uploaded logo as the header, and the following information below using the font Formal436bt:
• Open House!
• Feb 10th, March 10th and April 21st.
• Call 555 417-9086 for more information
Should not have
• Any other color but the red and white indicated on our logo

```html
<!DOCTYPE html>
<html lang="en">
<head>
<meta charset="utf-8">
<title>Brightfern School — Open House Yard Sign</title>
<link rel="stylesheet" href="https://fonts.googleapis.com/css2?family=Alegreya+Sans:wght@500;700&display=swap">
<style>
  :root {
    --backdrop: #1c1c1c;
    --red-deep: #9e111c;
    --red-bright: #ec1f27;
    --band-black: #000000;
    --white: #ffffff;
  }
  html, body {
    margin: 0;
    width: 1200px;
    height: 1000px;
    overflow: hidden;
    background: var(--backdrop);
  }
  .yard-sign {
    position: absolute;
    left: 275px;
    top: 65px;
    width: 650px;
    height: 870px;
    font-family: "Alegreya Sans", sans-serif;
    color: var(--white);
    text-align: center;
    font-variant-numeric: oldstyle-nums;
  }
  .sign-main {
    position: absolute;
    inset: 0 0 207px 0;
    background: linear-gradient(90deg, var(--red-deep) 0%, var(--red-bright) 100%);
  }
  .school-name {
    position: absolute;
    top: 98px;
    left: 0;
    right: 0;
    display: flex;
    justify-content: center;
    align-items: center;
    gap: 16px;
    font-size: 40px;
    font-weight: 500;
    letter-spacing: 1px;
    text-transform: uppercase;
  }
  .school-mark {
    width: 24px;
    height: 24px;
    background: var(--white);
  }
  .headline {
    position: absolute;
    top: 268px;
    left: 0;
    right: 0;
    margin: 0;
    font-size: 124px;
    font-weight: 500;
    line-height: 110px;
    text-transform: uppercase;
  }
  .divider {
    position: absolute;
    top: 514px;
    left: 80px;
    width: 488px;
    height: 2px;
    background: var(--white);
  }
  .dates {
    position: absolute;
    top: 540px;
    left: 0;
    right: 0;
    margin: 0;
    font-size: 45px;
    font-weight: 500;
    line-height: 48px;
  }
  .sign-footer {
    position: absolute;
    left: 0;
    right: 0;
    bottom: 0;
    height: 207px;
    background: var(--band-black);
  }
  .call {
    position: absolute;
    top: 42px;
    left: 0;
    right: 0;
    margin: 0;
    font-size: 62px;
    font-weight: 500;
    line-height: 64px;
  }
  .call-note {
    display: block;
    font-size: 42px;
    line-height: 52px;
  }
</style>
</head>
<body>
  <article class="yard-sign">
    <section class="sign-main">
      <header class="school-name">
        <span class="school-mark" aria-hidden="true"></span>
        <span>Brightfern School</span>
      </header>
      <h1 class="headline">Open<br>House!</h1>
      <div class="divider" aria-hidden="true"></div>
      <p class="dates">Feb 10th, March 10th<br>and April 21st.</p>
    </section>
    <footer class="sign-footer">
      <p class="call">Call 555 417-9086<span class="call-note">for more information</span></p>
    </footer>
  </article>
</body>
</html>
```